New business card for my lawn and landscape business

Dorrin Yard and Building is a full-service lawn care, landscaping, and light construction company serving Paragould and the Northeast Arkansas region. The business is owned and operated by Marcus Toller, with a reputation for hands-on, detail-oriented service, dependable crews, and quality results for both residential and commercial clients. A well regarded business with great reviews.
Owner Marcus Toller
Dorrinyardandbuilding.example

Target Market(s)

Commercial, Middle, and upper class in north east Arkansas

Industry/Entity Type

Lawn maintenance and landscape

Contact Information for Business Card

Dorrin Yard And Building Professional lawn care, landscaping, and property improvement in Northeast Arkansas. • lawn maintenance •lawn treatments and weed control • exterior projects • Custom landscape design & installation • Sod, trees, rock & drainage solutions • Residential & commercial services Reliable. Detailed. Done right.

Requirements
Must have
• Business name, service area, list of some of our services, clean design that represents
Nice to have
• Unique. Different design element than just grass because its already in n the logo. Picture of a warm season (south) lawn or landscape. Pictures of the type of work we do

```html
<!DOCTYPE html>
<html lang="en">
<head>
<meta charset="utf-8">
<title>Dorrin Yard and Building – Business Card</title>
<link href="https://fonts.googleapis.com/css2?family=Poppins:wght@300;400;500;600&display=swap" rel="stylesheet">
<style>
  :root {
    --ink: #111111;
    --card: #141414;
    --stage: #2a2a2a;
    --green: #7cb342;
    --green-deep: #5e9a2a;
    --steel: #7d7d7d;
    --paper: #f2f2f2;
  }
  * { margin: 0; padding: 0; box-sizing: border-box; }
  html, body {
    width: 1200px; height: 900px; overflow: hidden;
    background: var(--stage);
    font-family: "Poppins", sans-serif;
  }
  .canvas {
    position: relative; width: 1200px; height: 900px;
    display: flex; flex-direction: column; align-items: center;
    justify-content: center; gap: 40px;
  }
  .card {
    position: relative; width: 700px; height: 400px;
    background: var(--card); overflow: hidden;
    box-shadow: 0 12px 30px rgba(0,0,0,.5);
  }
  .card-art { position: absolute; inset: 0; width: 100%; height: 100%; }

  .brand { position: absolute; display: flex; align-items: center; gap: 14px; }
  .brand-dot {
    width: 64px; height: 64px; border-radius: 50%;
    border: 6px solid var(--steel); flex: none;
  }
  .brand-name {
    color: var(--green); font-weight: 600; font-size: 26px;
    line-height: 1.1; letter-spacing: 1px; text-transform: uppercase;
  }

  .front .brand { left: 48px; top: 150px; }
  .owner { position: absolute; right: 48px; top: 40px; text-align: right; }
  .owner-name { color: var(--green); font-weight: 600; font-size: 28px; line-height: 1.1; }
  .owner-role { color: var(--paper); font-weight: 300; font-size: 14px; }
  .edge-tab {
    position: absolute; right: 0; top: 36px; width: 12px; height: 46px;
    background: var(--green);
  }
  .contact {
    position: absolute; right: 30px; top: 195px;
    list-style: none; text-align: right; color: var(--ink);
    font-size: 17px; line-height: 1.45; font-weight: 400;
  }
  .contact li { display: flex; justify-content: flex-end; align-items: center; gap: 10px; }
  .contact .address { padding-right: 26px; }
  .contact svg { width: 16px; height: 16px; flex: none; }

  .back .brand { left: 56px; top: 120px; }
  .services { position: absolute; left: 360px; top: 60px; color: var(--paper); }
  .services-title {
    color: var(--green); font-weight: 500; font-size: 19px;
    text-transform: uppercase; margin-bottom: 4px;
  }
  .services ul { list-style: none; font-size: 13.5px; font-weight: 300; line-height: 1.55; }
  .services li::before { content: "• "; color: var(--green); }
  .tagline { font-size: 13.5px; font-weight: 300; margin-top: 2px; padding-left: 10px; }
  .grass-band {
    position: absolute; left: 0; right: 0; bottom: 0; height: 110px;
    background: linear-gradient(to bottom, rgba(124,179,66,0) 0%, var(--green-deep) 55%, var(--green) 100%);
  }
</style>
</head>
<body>
<main class="canvas">

  <section class="card front">
    <svg class="card-art" viewBox="0 0 700 400" preserveAspectRatio="none" aria-hidden="true">
      <path d="M0,320 C250,330 330,185 450,160 C560,138 630,132 700,128 L700,400 L0,400 Z" fill="var(--green)"/>
      <path d="M390,185 C470,120 570,108 700,108" fill="none" stroke="var(--steel)" stroke-width="14"/>
      <path d="M150,345 C270,330 330,270 380,215 C340,280 270,335 150,345 Z" fill="var(--ink)"/>
    </svg>
    <div class="edge-tab"></div>
    <div class="brand">
      <span class="brand-dot"></span>
      <span class="brand-name">Dorrin Yard<br>&amp; Building</span>
    </div>
    <div class="owner">
      <p class="owner-name">Marcus Toller</p>
      <p class="owner-role">Owner</p>
    </div>
    <ul class="contact">
      <li class="address">Fernmoor, XY</li>
      <li class="address">United States, Sample State</li>
      <li>+1 555-014-2290
        <svg viewBox="0 0 16 16"><path d="M3 1h3l1.5 4-2 1.3a9 9 0 0 0 4.2 4.2L11 8.5l4 1.5v3a2 2 0 0 1-2 2A12 12 0 0 1 1 3a2 2 0 0 1 2-2z" fill="var(--ink)"/></svg></li>
      <li>Dorrinyardandbuilding@mail.example
        <svg viewBox="0 0 16 16"><rect x="1" y="3" width="14" height="10" fill="var(--ink)"/><path d="M1 3l7 6 7-6" fill="none" stroke="var(--green)" stroke-width="1.4"/></svg></li>
      <li>Dorrinyardandbuilding.example
        <svg viewBox="0 0 16 16"><circle cx="8" cy="8" r="7" fill="var(--ink)"/><path d="M1 8h14M8 1c-3 3-3 11 0 14M8 1c3 3 3 11 0 14" fill="none" stroke="var(--green)" stroke-width="1"/></svg></li>
    </ul>
  </section>

  <section class="card back">
    <div class="grass-band" role="img" aria-label="Illustrated blades of green grass along the bottom edge"></div>
    <div class="brand">
      <span class="brand-dot"></span>
      <span class="brand-name">Dorrin Yard<br>&amp; Building</span>
    </div>
    <div class="services">
      <h2 class="services-title">Our Services</h2>
      <ul>
        <li>Lawn maintenance</li>
        <li>Lawn treatments and weed control</li>
        <li>Exterior projects</li>
        <li>Custom landscape design &amp; installation</li>
        <li>Sod, trees, rock &amp; drainage solutions</li>
        <li>Residential &amp; commercial services</li>
      </ul>
      <p class="tagline">Reliable. Detailed. Done right.</p>
    </div>
  </section>

</main>
</body>
</html>
```